Instagram Business Card For Comedian

Hi,

I'd like a 2-sided business card that kind mimics an Instagram page. I've attached screenshots with the copy and language that should be written on there.

I'd like it to be way more stylized and a bit more creative than what I did on Powerpoint. I just did a mockup so that you can have an idea. I'd like it to be designed and you to take a bit of creative imagery so that it doesn't look so static and monochromatic.

PLEASE BE CREATIVE WITH THESE DESIGNS. I DON'T WANT IT TO LOOK EXACTLY LIKE THE ATTACHED IMAGE OR EXACTLY LIKE AN INSTAGRAM PAGE. I want to use it as inspiration to create something that looks more sleek, and creative. I don't want the colors to just be boring gray, and blue. Have fun and spice it up a bit!

Check out my website LornaFabish.com to see the colors and fonts I use for my branding.

For the main photo: Here's a link with the hi-res photo: !https://www.filecrate-example.com/s/q8ktw3rmpadvhje/Lorna-Fabish-C71B2204.jpg?dl=0

For the thumbnail icon photo, you can use this: https://www.filecrate-example.com/s/xo5nvte2gwhrbsk/Lorna%20Fabish%20Tin%20Vale%20Headshot.jpg?dl=0

Use the Standard Business Card Template from Quillprint.com:
https://help.quillprint-example.com/hc/en-us/article_attachments/309827164/Standard_Size__US__Business_Cards_Portrait.jpg

Please let me know if you have any questions.
Updates

Industry/Entity Type

Business

Contact Information for Business Card

All of the text and copy has been provided on the attached jpg.

Colors
33a6d7
0255a3
aaaaaa
dbdbdb
1b1b1b

Requirements
Should not have
• A Hyperlink for the Email Addresses

```html
<!DOCTYPE html>
<html lang="en">
<head>
<meta charset="utf-8">
<title>Lorna Fabish – Business Card</title>
<link href="https://fonts.googleapis.com/css2?family=PT+Sans:wght@400;700&display=swap" rel="stylesheet">
<style>
  :root {
    --stage: #3d3938;
    --card: #ffffff;
    --card-alt: #f7f7f7;
    --band: #e3e3e3;
    --band-light: #ececec;
    --brand-blue: #1462a3;
    --link-blue: #2f6fb8;
    --ink: #1b1b1b;
    --ink-soft: #3a3a3a;
    --icon: #4a4a4a;
    --rule: #aaaaaa;
  }
  * { margin: 0; padding: 0; box-sizing: border-box; }
  html, body { width: 1200px; height: 900px; overflow: hidden; }
  body {
    background: var(--stage);
    font-family: "PT Sans", "Helvetica Neue", Arial, sans-serif;
    color: var(--ink);
    position: relative;
  }
  .card {
    position: absolute;
    top: 184px;
    height: 491px;
    box-shadow: 4px 4px 6px rgba(0,0,0,.55);
    overflow: hidden;
  }
  .card--front { left: 322px; width: 301px; background: var(--card); }
  .card--back { left: 645px; width: 305px; background: var(--card-alt); }
  .abs { position: absolute; }

  /* front */
  .post-avatar { left: 11px; top: 7px; width: 31px; height: 31px; border-radius: 50%;
    background: radial-gradient(circle at 50% 40%, #7a4a32, #2a1b16 70%); }
  .post-user { left: 49px; top: 7px; font-size: 14px; font-weight: 700; line-height: 1; }
  .post-location { left: 49px; top: 22px; font-size: 13px; color: var(--link-blue); line-height: 1; }
  .post-photo { left: 0; top: 42px; width: 301px; height: 289px;
    background: linear-gradient(180deg, #ece8e4 0%, #5a3a2c 30%, #3a241c 60%, #e06c55 85%, #e87a62 100%); }
  .post-actions { left: 16px; top: 334px; }
  .post-rule { left: 14px; top: 353px; width: 272px; height: 1px; background: var(--rule); }
  .post-likes { left: 15px; top: 362px; font-size: 12px; font-weight: 700; color: var(--link-blue);
    display: flex; align-items: center; gap: 4px; }
  .post-caption { left: 14px; top: 380px; width: 280px; font-size: 12px; line-height: 15.6px; color: var(--ink-soft); }
  .post-caption strong { color: var(--ink); font-size: 13px; }

  /* back */
  .profile-header { left: 0; top: 0; width: 100%; height: 42px; background: var(--brand-blue);
    color: #fff; font-weight: 700; font-size: 20px; display: flex; align-items: center; justify-content: center; letter-spacing: .3px; }
  .profile-strip { left: 0; top: 42px; width: 100%; height: 19px; background: var(--band-light); }
  .profile-avatar { left: 226px; top: 43px; width: 64px; height: 64px; border-radius: 50%;
    border: 1px solid #fff; background: radial-gradient(circle at 50% 45%, #6b3e2a, #1e1411 70%); }
  .row-icon { left: 20px; }
  .profile-name { left: 56px; top: 86px; font-size: 14px; font-weight: 700; letter-spacing: .3px; }
  .profile-role { left: 56px; top: 104px; font-size: 10px; letter-spacing: .2px; }
  .profile-site { left: 56px; top: 130px; font-size: 14px; letter-spacing: .2px; }
  .profile-contact { left: 59px; top: 160px; font-size: 12px; line-height: 14px; }
  .profile-contact small { font-size: 10px; display: block; }
  .section-band { left: 0; width: 100%; height: 29px; background: var(--band);
    font-size: 16px; font-weight: 700; color: #444; padding-left: 25px; display: flex; align-items: center; }
  .about-text { left: 26px; top: 247px; width: 252px; font-size: 13.5px; line-height: 15px; color: var(--ink-soft); }
  .about-text p + p { margin-top: 3px; }
  .more-links { left: 24px; top: 389px; font-size: 12px; line-height: 15px; color: var(--ink-soft); }
  .signoff { left: 0; top: 457px; width: 100%; text-align: center; font-size: 12px; color: var(--ink-soft); }
</style>
</head>
<body>

<section class="card card--front" aria-label="Front of card">
  <div class="abs post-avatar" role="img" aria-label="Small round profile photo of Lorna Fabish"></div>
  <div class="abs post-user">fabishly</div>
  <div class="abs post-location">Brooklyn, New York</div>
  <div class="abs post-photo" role="img" aria-label="Portrait photo of Lorna Fabish in a coral top"></div>
  <svg class="abs post-actions" width="270" height="16" viewBox="0 0 270 16" fill="none" stroke="#555" stroke-width="1.2">
    <path d="M8 14 C2 9 0 6 2 3.5 C4 1 7 2 8 4.5 C9 2 12 1 14 3.5 C16 6 14 9 8 14Z"/>
    <circle cx="30" cy="8" r="6.3"/><path d="M25 12 L24 15 L27.5 13.5"/>
    <path d="M45 14 V10 Q45 6 50 6 H57"/><path d="M54 3 L57.5 6 L54 9"/>
    <g fill="#888" stroke="none"><circle cx="252" cy="8" r="1.1"/><circle cx="256" cy="8" r="1.1"/><circle cx="260" cy="8" r="1.1"/><circle cx="264" cy="8" r="1.1"/></g>
  </svg>
  <div class="abs post-rule"></div>
  <div class="abs post-likes">
    <svg width="11" height="10" viewBox="0 0 16 14"><path fill="#2f6fb8" d="M8 14 C2 9 0 6 2 3 C4 0 7 1 8 4 C9 1 12 0 14 3 C16 6 14 9 8 14Z"/></svg>
    321 LIKES
  </div>
  <div class="abs post-caption">
    <strong>fabishly</strong> Your favorite comic's favorite comic.<br>
    #ISAIDIT #SOITSTRUE #FINDME #FOLLOWME<br>
    #NOTTOMYHOUSE # POSTABOUTMEUSINGTHESE-<br>
    HASHTAGS #LORNAFABISH #FABISHLY<br>
    #IMSUCHABROOKLYNGIRL #MAKENYUNSAFEAGAIN<br>
    #BROOKLYNSTANDUPCOMEDY
  </div>
</section>

<section class="card card--back" aria-label="Back of card">
  <div class="abs profile-header">EDIT PROFILE</div>
  <div class="abs profile-strip"></div>
  <div class="abs profile-avatar" role="img" aria-label="Round headshot of Lorna Fabish"></div>

  <svg class="abs row-icon" style="top:85px" width="28" height="28" viewBox="0 0 28 28" fill="var(--icon)">
    <circle cx="14" cy="8" r="6"/><path d="M2 28 V22 Q2 15 10 15 H18 Q26 15 26 22 V28Z"/>
  </svg>
  <div class="abs profile-name">LORNA FABISH</div>
  <div class="abs profile-role">COMEDIAN | ACTOR | WRITER</div>

  <svg class="abs row-icon" style="top:127px" width="24" height="24" viewBox="0 0 24 24">
    <circle cx="12" cy="12" r="11" fill="var(--icon)"/>
    <path fill="#f7f7f7" d="M6 7 Q9 5 11 7 L10 10 L7 11 Z M13 11 L17 11 L18 15 L15 19 L13 16 Z M15 5 L18 6 L17 8 Z"/>
  </svg>
  <div class="abs profile-site">WWW.LORNAFABISH.COM</div>

  <svg class="abs row-icon" style="left:25px;top:178px" width="22" height="18" viewBox="0 0 22 18" fill="none" stroke="var(--icon)" stroke-width="1.4">
    <rect x="1" y="1" width="20" height="16"/><path d="M1 1 L11 10 L21 1 M1 17 L8 8 M21 17 L14 8"/>
  </svg>
  <div class="abs profile-contact">
    <small>For Bookings:</small>
    Dana@BrightPierTalent.com<br>
    Mara.Quill@velnova.com
  </div>

  <div class="abs section-band" style="top:211px">ABOUT ME</div>
  <div class="abs about-text">
    <p>Stand Up Comedian. I Host. I write. I Dance. I Do Not Sing Unless I'm in the Shower. I Accept Tips. (Not on jokes, but on PayPing.</p>
    <p>As seen on Northline, Laugh Channel, Pulse TV, Reel TV, Outset, and Crown.</p>
  </div>

  <div class="abs section-band" style="top:351px">MORE INFO</div>
  <div class="abs more-links">
    FACEFEED.COM/LORNAFABISH<br>
    CHIRPLY.COM/FABISHLY<br>
    SNAPGRID.COM/FABISHLY
  </div>
  <div class="abs signoff">Lets Stay Connected !</div>
</section>

</body>
</html>
```